Letterhead and Stationary for Construction Company

Lumen Forge needs modern Letterhead, Envelopes and Notepad designs.

Industry/Entity Type

Construction

Colors
f78f20
34a7d8
ffffff

Requirements
Must have
• Modern looking design.

```html
<!DOCTYPE html>
<html lang="en">
<head>
<meta charset="utf-8">
<title>Lumen Forge Stationery</title>
<link rel="stylesheet" href="https://fonts.googleapis.com/css2?family=Arimo:wght@400;700&family=Exo+2:wght@400;500&display=swap">
<style>
  :root {
    --orange: #f07f35;
    --blue: #3179c1;
    --paper: #ffffff;
    --backdrop: #ebebeb;
    --ink: #3a3a3a;
    --ink-soft: #555555;
    --icon: #3d3d3d;
  }
  * { box-sizing: border-box; margin: 0; padding: 0; }
  html, body { width: 1200px; height: 938px; overflow: hidden; }
  body { background: var(--backdrop); position: relative; font-family: "Arimo", Arial, sans-serif; color: var(--ink); }

  .sheet { position: absolute; background: var(--paper); box-shadow: 0 2px 6px rgba(0,0,0,0.12); overflow: hidden; }

  .brand { position: absolute; display: flex; align-items: center; font-family: "Exo 2", sans-serif; font-weight: 500; color: var(--blue); white-space: nowrap; }
  .brand-dot { border-radius: 50%; background: var(--orange); flex: none; }

  .band { position: absolute; height: 100%; top: 0; }
  .band-row { position: absolute; left: 0; right: 0; }
  .band-orange { background: var(--orange); left: 0; }
  .band-blue { background: var(--blue); right: 0; color: #fff; font-family: "Exo 2", sans-serif; display: flex; align-items: center; justify-content: center; letter-spacing: 0.06em; }

  .contact-list { position: absolute; list-style: none; font-size: 4.4px; color: var(--ink-soft); }
  .contact-list li { display: flex; align-items: center; height: 8.4px; }
  .contact-list .ico { width: 5px; height: 5px; background: var(--icon); margin-right: 4px; flex: none; }

  /* Letterhead */
  .letterhead { left: 184px; top: 67px; width: 388px; height: 546px; }
  .letterhead .brand { left: 17px; top: 34px; font-size: 19px; }
  .letterhead .brand-dot { width: 24px; height: 24px; margin-right: 6px; }
  .letter-body { position: absolute; left: 37px; top: 139px; width: 296px; font-size: 5.4px; line-height: 8.4px; color: var(--ink); }
  .letter-body p { margin-bottom: 8px; }
  .letter-body .gap { margin-bottom: 24px; }
  .letter-body strong { font-weight: 700; }
  .signature { width: 40px; height: 26px; background: #f1f1f1; margin: 4px 0 8px; }
  .letterhead .band-row { top: 488px; height: 16px; }
  .letterhead .band-orange { width: 118px; }
  .letterhead .band-blue { width: 267px; font-size: 9.5px; }
  .letterhead .contact-left { left: 9px; top: 513px; }
  .letterhead .contact-right { left: 318px; top: 513px; }

  /* Folder */
  .folder { left: 636px; top: 40px; width: 458px; height: 576px; }
  .folder .brand { left: 0; right: 0; top: 268px; justify-content: center; font-size: 30px; }
  .folder .brand-dot { width: 40px; height: 40px; margin-right: 10px; }
  .folder .band-row { top: 524px; height: 28px; }
  .folder .band-orange { width: 140px; }
  .folder .band-blue { width: 315px; font-size: 12.5px; }

  /* Business cards */
  .card-front { left: 46px; top: 660px; width: 176px; height: 99px; }
  .card-front .brand { left: 8px; top: 12px; font-size: 13px; }
  .card-front .brand-dot { width: 16px; height: 16px; margin-right: 4px; }
  .holder { position: absolute; left: 123px; top: 15px; font-family: "Exo 2", sans-serif; }
  .holder-name { font-size: 6.6px; letter-spacing: 0.05em; color: var(--ink); }
  .holder-role { font-size: 4.2px; letter-spacing: 0.05em; color: var(--ink-soft); margin-top: 2px; }
  .card-front .band-row { top: 42px; height: 16px; }
  .card-front .band-orange { width: 54px; }
  .card-front .band-blue { width: 120px; font-size: 5.8px; }
  .card-front .contact-list { font-size: 3.8px; }
  .card-front .contact-list li { height: 9px; }
  .card-front .contact-list .ico { width: 6px; height: 6px; margin-right: 3px; }
  .card-front .contact-left { left: 9px; top: 66px; }
  .card-front .contact-right { left: 109px; top: 66px; }

  .card-back { left: 46px; top: 785px; width: 176px; height: 100px; }
  .card-back .brand { left: 0; right: 0; top: 40px; justify-content: center; font-size: 15px; }
  .card-back .brand-dot { width: 20px; height: 20px; margin-right: 5px; }

  /* Envelope front */
  .envelope-front { left: 266px; top: 674px; width: 431px; height: 207px; }
  .envelope-front .brand { left: 14px; top: 28px; font-size: 16px; }
  .envelope-front .brand-dot { width: 22px; height: 22px; margin-right: 5px; }
  .envelope-front .band-row { top: 164px; height: 19px; }
  .envelope-front .band-orange { width: 132px; }
  .envelope-front .band-blue { width: 297px; font-size: 10px; }

  /* Envelope back */
  .envelope-back { left: 737px; top: 673px; width: 432px; height: 207px; }
  .envelope-flap { position: absolute; left: 0; top: 0; width: 100%; height: 71px; background: var(--blue); border-radius: 0 0 38px 38px; display: flex; align-items: center; justify-content: center; color: #fff; font-family: "Exo 2", sans-serif; font-size: 13px; letter-spacing: 0.06em; }
</style>
</head>
<body>

<section class="sheet letterhead" aria-label="Letterhead">
  <div class="brand"><span class="brand-dot"></span>Lumen Forge</div>
  <div class="letter-body">
    <p>July 2, 2012</p>
    <p><strong>Dear CH,</strong><br>Forge House, 18 Mill Lane, Harbor City</p>
    <p>We are pleased to confirm the start of works on your site next month. Our crew will deliver framing, roofing and finishing under one schedule, with weekly progress reports and a single point of contact for every question you may have. All materials are sourced locally and inspected before installation, and safety briefings take place each morning.</p>
    <p class="gap">Please review the attached plan and confirm access times for delivery vehicles and the site crane before the first week.</p>
    <p>Once the foundation is complete we will share photos and a revised timeline. Any change to the scope can be agreed in writing with our site manager, who will update costs within two working days. We thank you for choosing us and look forward to building a structure that will serve you well for many years ahead.</p>
    <p>Best Regards,</p>
    <div class="signature" role="img" aria-label="Handwritten signature"></div>
    <p><strong>Dana Whitlock</strong><br>Director</p>
    <p>Forge House, 18 Mill Lane, Harbor City</p>
  </div>
  <div class="band-row">
    <div class="band band-orange"></div>
    <div class="band band-blue">www.lumenforge-build.com</div>
  </div>
  <ul class="contact-list contact-left">
    <li><span class="ico"></span>18 Mill Lane</li>
    <li><span class="ico"></span>014 552 7830</li>
    <li><span class="ico"></span>hello@lumenforge-build.com</li>
  </ul>
  <ul class="contact-list contact-right">
    <li><span class="ico"></span>www.lumenforge-build.com</li>
    <li><span class="ico"></span>@lumenforge</li>
    <li><span class="ico"></span>/lumenforgebuild</li>
  </ul>
</section>

<section class="sheet folder" aria-label="Presentation folder">
  <div class="brand"><span class="brand-dot"></span>Lumen Forge</div>
  <div class="band-row">
    <div class="band band-orange"></div>
    <div class="band band-blue">www.lumenforge-build.com</div>
  </div>
</section>

<section class="sheet card-front" aria-label="Business card front">
  <div class="brand"><span class="brand-dot"></span>Lumen Forge</div>
  <div class="holder">
    <div class="holder-name">OWEN CARRICK</div>
    <div class="holder-role">MANAGER</div>
  </div>
  <div class="band-row">
    <div class="band band-orange"></div>
    <div class="band band-blue">www.lumenforge-build.com/123</div>
  </div>
  <ul class="contact-list contact-left">
    <li><span class="ico"></span>18 Mill Lane</li>
    <li><span class="ico"></span>014 552 7830</li>
    <li><span class="ico"></span>hello@lumenforge-build.com</li>
  </ul>
  <ul class="contact-list contact-right">
    <li><span class="ico"></span>www.lumenforge-build.com</li>
    <li><span class="ico"></span>@lumenforge</li>
    <li><span class="ico"></span>/lumenforgebuild</li>
  </ul>
</section>

<section class="sheet card-back" aria-label="Business card back">
  <div class="brand"><span class="brand-dot"></span>Lumen Forge</div>
</section>

<section class="sheet envelope-front" aria-label="Envelope front">
  <div class="brand"><span class="brand-dot"></span>Lumen Forge</div>
  <div class="band-row">
    <div class="band band-orange"></div>
    <div class="band band-blue">www.lumenforge-build.com</div>
  </div>
</section>

<section class="sheet envelope-back" aria-label="Envelope back">
  <div class="envelope-flap">www.lumenforge-build.com</div>
</section>

</body>
</html>
```